Double sided business Card voor Luchtkoel Brederwijk

Card design must be in line with our logo. Clean and professional look. Colors can be used, but not too wild.
Logo in frontside. Details on the backside. We want a qr in the design.

Details: (person)
name: Maarten Bosveld
tel: 06-48271935
maarten@luchtkoelbrederwijk.nl

tel: 088-5063918 (business general)
info@luchtkoelbrederwijk.nl

.

```html
<!DOCTYPE html>
<html lang="nl">
<head>
<meta charset="utf-8">
<title>Luchtkoel Brederwijk – visitekaartje</title>
<link href="https://fonts.googleapis.com/css2?family=Arimo:wght@400;500&display=swap" rel="stylesheet">
<style>
  :root {
    --stage: #2e2e2e;
    --brand-blue: #0a5fbf;
    --brand-blue-deep: #0a3f95;
    --brand-blue-light: #35a6ea;
    --brand-red: #e61e28;
    --paper: #ffffff;
    --ink: #3a3a3a;
    --ink-soft: #555555;
  }
  * { margin: 0; padding: 0; box-sizing: border-box; }
  html, body { width: 1200px; height: 689px; overflow: hidden; }
  body {
    background: var(--stage);
    font-family: "Arimo", Arial, sans-serif;
    position: relative;
  }
  .card {
    position: absolute;
    top: 174px;
    width: 540px;
    height: 340px;
    border-radius: 22px;
    overflow: hidden;
  }
  .card-front { left: 30px; }
  .card-back { left: 630px; background: var(--paper); }

  /* Front: embossed brand-pattern area rendered as a soft tonal field */
  .front-pattern {
    position: absolute; inset: 0;
    background:
      radial-gradient(ellipse 70% 60% at 85% 10%, rgba(120, 215, 255, 0.55), transparent 70%),
      linear-gradient(200deg, var(--brand-blue-light) 0%, var(--brand-blue) 45%, var(--brand-blue-deep) 100%);
  }
  .front-mark {
    position: absolute; right: 40px; top: 120px;
    color: var(--paper);
    font-size: 13px; letter-spacing: 2px;
    display: flex; align-items: center; gap: 8px;
  }
  .front-mark .dot { width: 12px; height: 12px; border-radius: 50%; background: var(--paper); }

  .back-shapes { position: absolute; inset: 0; width: 100%; height: 100%; }

  .holder-name {
    position: absolute; right: 34px; top: 30px;
    color: var(--paper);
    font-size: 22px; font-weight: 400; letter-spacing: 0.5px;
  }
  .brand {
    position: absolute; left: 128px; top: 200px;
    display: flex; align-items: center; gap: 12px;
  }
  .brand .dot { width: 22px; height: 22px; border-radius: 50%; background: var(--brand-red); }
  .brand-name {
    color: var(--ink-soft);
    font-size: 15px; letter-spacing: 3px; line-height: 1.35;
    text-transform: uppercase;
  }
  .contact {
    position: absolute; right: 30px; top: 128px;
    text-align: right;
    color: var(--ink);
    font-size: 12.5px; line-height: 17px;
  }
  .contact-group + .contact-group { margin-top: 14px; }
  .contact-line { display: flex; justify-content: flex-end; align-items: center; gap: 6px; }
  .contact-line svg { width: 11px; height: 11px; flex: none; }
  .icon-spacer { width: 11px; flex: none; }

  .qr-slot {
    position: absolute; right: 30px; bottom: 24px;
    width: 62px; height: 62px;
    border: 2px solid var(--ink);
    border-radius: 4px;
    background: var(--paper);
  }
</style>
</head>
<body>

  <section class="card card-front" aria-label="Voorzijde">
    <div class="front-pattern" role="img" aria-label="Blauw reliëfpatroon van het beeldmerk"></div>
    <div class="front-mark"><span class="dot"></span><span>LUCHTKOEL BREDERWIJK</span></div>
  </section>

  <section class="card card-back" aria-label="Achterzijde">
    <svg class="back-shapes" viewBox="0 0 540 340" preserveAspectRatio="none" aria-hidden="true">
      <rect width="540" height="340" fill="var(--brand-blue)"/>
      <path d="M540 86 C290 80 38 146 44 268 C47 310 120 334 250 340 L300 340 C130 330 72 305 74 266 C80 160 300 100 540 98 Z" fill="var(--brand-red)"/>
      <path d="M540 98 C300 100 80 160 74 266 C72 305 130 330 300 340 L540 340 Z" fill="var(--paper)"/>
    </svg>

    <div class="holder-name">MAARTEN BOSVELD</div>

    <div class="brand">
      <span class="dot"></span>
      <div class="brand-name">Luchtkoel<br>Brederwijk</div>
    </div>

    <div class="contact">
      <div class="contact-group">
        <div class="contact-line"><span>06-48271935</span><span class="icon-spacer"></span></div>
        <div class="contact-line"><span>maarten@luchtkoelbrederwijk.nl</span><span class="icon-spacer"></span></div>
      </div>
      <div class="contact-group">
        <div class="contact-line"><span>088-5063918</span>
          <svg viewBox="0 0 12 12"><path d="M3 1 L5 3.5 L4 5 C4.8 6.6 5.6 7.4 7 8 L8.5 7 L11 9 L9.6 11 C5 10.5 1.5 7 1 2.4 Z" fill="var(--brand-red)"/></svg>
        </div>
        <div class="contact-line"><span>info@luchtkoelbrederwijk.nl</span>
          <svg viewBox="0 0 12 12"><rect x="0.5" y="2" width="11" height="8" fill="var(--brand-red)"/><path d="M0.5 2 L6 6.5 L11.5 2" stroke="#fff" fill="none"/></svg>
        </div>
        <div class="contact-line"><span>www.luchtkoelbrederwijk.nl</span>
          <svg viewBox="0 0 12 12"><circle cx="6" cy="6" r="5.5" fill="var(--brand-red)"/><path d="M0.5 6 H11.5 M6 0.5 C3 3 3 9 6 11.5 C9 9 9 3 6 0.5" stroke="#fff" stroke-width="0.8" fill="none"/></svg>
        </div>
      </div>
    </div>

    <div class="qr-slot" role="img" aria-label="Plaats voor QR-code naar de website"></div>
  </section>

</body>
</html>
```